Christmas Postcard a manufacturer of skirting boards

Relaunch of the Christmas greetings Postcard of a company manufacturing premium quality skirting boards from real wood. Please refer to http://www.brumholt-profile.example/

- Christmas greetings Postcard 105 mm x 210 mm (card will be sent without envelope)

frontside:
- your graphic design, including
- Logo on the card
- Greetings "Frohe Weihnachten und ein erfolgreiches neues Jahr" on the card (front)
- insert Wooden Earring(s) - for recognition!

backside: (on the left)
"Wir bedanken uns für die partnerschaftliche Zusammenarbeit und freuen uns darauf, Sie auch im Jahr 2016 mit unseren Angeboten, Ideen und Know-how bei der Verwirklichung Ihrer Vorhaben zu unterstützen. (see pdf´s)

Ihnen und Ihren Mitarbeitern wünschen wir ein zauberhaftes Weihnachtsfest und für das neue Jahr Gesundheit, Glück, Erfolg und Freude."

Signatures (see pdf`s)

backside (on the right):
Adress field

------
The pdf´s from last years are just for the color mood. Fresh, modern design appreciated, no comic style.

Industry/Entity Type

It Company

Requirements
Must have
• "Wooden Earring(s)"

```html
<!DOCTYPE html>
<html lang="de">
<head>
<meta charset="utf-8">
<title>Weihnachtskarte Brumholt Leistenfabrik</title>
<link href="https://fonts.googleapis.com/css2?family=Dancing+Script:wght@700&family=Hind:wght@300;400;700&display=swap" rel="stylesheet">
<style>
  :root {
    --backdrop: #d9d9db;
    --paper: #ffffff;
    --greeting-red: #b8202c;
    --stripe-red: #b01f2a;
    --band-tan: #e8bf90;
    --ink: #2b2b2b;
    --ink-soft: #555555;
    --sig-grey: #e4e4e4;
    --photo-sky: #cfdde6;
    --photo-snow: #f4f1ec;
    --photo-warm: #e9d2b4;
  }
  * { box-sizing: border-box; margin: 0; padding: 0; }
  html, body { width: 1200px; height: 900px; overflow: hidden; }
  body { background: var(--backdrop); position: relative; font-family: "Hind", sans-serif; }

  .card {
    position: absolute; top: 32px; width: 419px; height: 835px;
    background: var(--paper); overflow: hidden;
    box-shadow: 0 2px 8px rgba(0,0,0,0.18);
  }
  .card--front { left: 128px; }
  .card--back { left: 644px; }

  .greeting {
    position: absolute; top: 34px; left: 0; width: 100%; z-index: 2;
    text-align: center; color: var(--greeting-red);
    font-family: "Dancing Script", cursive; font-weight: 700;
    font-size: 56px; line-height: 67px;
  }

  .winter-photo {
    position: absolute; top: 250px; left: 0; width: 100%; height: 483px; z-index: 1;
    background: linear-gradient(180deg, var(--paper) 0%, var(--paper) 12%, var(--photo-sky) 35%, var(--photo-snow) 60%, var(--photo-warm) 78%, var(--photo-snow) 100%);
  }

  .brand-footer { position: absolute; left: 0; bottom: 0; width: 100%; height: 134px; z-index: 3; }
  .brand-footer__stripe { position: absolute; top: 0; left: 0; width: 100%; height: 10px; background: var(--stripe-red); }
  .brand-footer__band { position: absolute; top: 10px; left: 0; width: 100%; height: 124px; background: var(--band-tan); }
  .brand-footer__rule { position: absolute; top: 64px; left: 0; width: 100%; height: 3px; background: var(--paper); }
  .brand-mark {
    position: absolute; top: 26px; left: 60px; display: flex; align-items: center; gap: 14px;
  }
  .brand-mark__square { width: 44px; height: 44px; background: var(--stripe-red); }
  .brand-mark__name {
    font-family: "Hind", sans-serif; font-weight: 700; font-size: 50px; line-height: 1;
    color: var(--paper); letter-spacing: 2px; padding-top: 8px;
  }
  .brand-footer__tagline {
    position: absolute; top: 86px; left: 0; width: 100%; text-align: center;
    font-family: "Hind", sans-serif; font-weight: 400; font-size: 20px;
    letter-spacing: 3px; color: var(--ink);
  }

  .message {
    position: absolute; top: 128px; left: 20px; right: 20px; text-align: center;
    font-weight: 300; font-size: 20px; line-height: 36px; color: var(--ink);
  }
  .message p + p { margin-top: 36px; }

  .signatures {
    position: absolute; top: 626px; left: 14px; right: 14px;
    display: flex; justify-content: space-between;
  }
  .signature { width: 120px; text-align: center; }
  .signature__stroke { display: block; width: 100px; height: 34px; margin: 0 auto; background: var(--sig-grey); border-radius: 4px; }
  .signature__name { display: block; margin-top: 10px; font-size: 8px; color: var(--ink-soft); }
</style>
</head>
<body>
  <section class="card card--front">
    <h1 class="greeting">Frohe<br>Weihnachten und<br>ein erfolgreiches<br>neues Jahr</h1>
    <div class="winter-photo" role="img" aria-label="Foto: zwei Schneemänner mit Mützen und Schals im Schnee, mit Holzohrringen"></div>
    <footer class="brand-footer">
      <div class="brand-footer__stripe"></div>
      <div class="brand-footer__band"></div>
      <div class="brand-footer__rule"></div>
      <div class="brand-mark">
        <span class="brand-mark__square"></span>
        <span class="brand-mark__name">BRUMHOLT</span>
      </div>
      <div class="brand-footer__tagline">Leistenfabrik Holzimport</div>
    </footer>
  </section>

  <section class="card card--back">
    <div class="message">
      <p>"Wir bedanken uns für die partnerschaft-<br>liche Zusammenarbeit und freuen uns<br>darauf, Sie auch im Jahr 2016 mit<br>unseren Angeboten, Ideen und Know-how<br>bei der Verwirklichung Ihrer Vorhaben zu<br>unterstützen. (see pdf´s)</p>
      <p>Ihnen und Ihren Mitarbeitern wünschen<br>wir ein zauberhaftes Weihnachtsfest und<br>für das neue Jahr Gesundheit, Glück,<br>Erfolg und Freude."</p>
    </div>
    <div class="signatures">
      <div class="signature"><span class="signature__stroke" role="img" aria-label="Unterschrift Jürgen Wendlinger"></span><span class="signature__name">Jürgen Wendlinger</span></div>
      <div class="signature"><span class="signature__stroke" role="img" aria-label="Unterschrift Margarete Wendlinger"></span><span class="signature__name">Margarete Wendlinger</span></div>
      <div class="signature"><span class="signature__stroke" role="img" aria-label="Unterschrift Florian Wendlinger"></span><span class="signature__name">Florian Wendlinger</span></div>
    </div>
    <footer class="brand-footer">
      <div class="brand-footer__stripe"></div>
      <div class="brand-footer__band"></div>
      <div class="brand-footer__rule"></div>
      <div class="brand-mark">
        <span class="brand-mark__square"></span>
        <span class="brand-mark__name">BRUMHOLT</span>
      </div>
      <div class="brand-footer__tagline">Leistenfabrik Holzimport</div>
    </footer>
  </section>
</body>
</html>
```